Modern Poster Needed for Video Gaming Related Site

Pixelhavenspots.com is looking for a talented designer to create a unique, modern, and captivating poser capturing our brand/logo. Our website is dedicated to video gamers who are looking for unique video gaming locations (like a directory) scatter throughout america and creating an exclusive community for those who live the gamer life.
The overall design should include the attached logo somehow and with a tag line: "Find Your Game" somewhere in the design. For the style we would like to see a modern/simple but eye catching design. Lastly if possible a footer with our site address: www.pixelhavenspots.com with regard to text style we will leave this up to your imagination. Thank you for you consideration and checking out our project. Good luck to all of you and we look forward to seeing what extraordinary works you come up with.

```html
<!DOCTYPE html>
<html lang="en">
<head>
<meta charset="UTF-8">
<title>Find Your Game – Pixel Haven Spots Poster</title>
<link href="https://fonts.googleapis.com/css2?family=Arimo:wght@700&display=swap" rel="stylesheet">
<style>
  :root {
    --backdrop: #e9e9e7;
    --paper: #ffffff;
    --band-black: #1b1b1b;
    --band-blue: #2b4fa9;
    --band-coral: #e8634f;
    --headline-text: #ffffff;
    --brand-orange: #e8542c;
    --ink: #1a1a1a;
    --map-light: #f1ede0;
    --map-mid: #d9d4bf;
  }
  * { margin: 0; padding: 0; box-sizing: border-box; }
  html, body {
    width: 1200px;
    height: 1148px;
    overflow: hidden;
    background: var(--backdrop);
    font-family: "Arimo", Arial, sans-serif;
  }
  .poster {
    position: absolute;
    left: 220px;
    top: 44px;
    width: 760px;
    height: 1060px;
    background: var(--paper);
  }
  .tagline {
    position: absolute;
    left: 90px;
    top: 100px;
    width: 580px;
  }
  .tagline__band {
    height: 150px;
    display: flex;
    align-items: center;
    padding-left: 46px;
    color: var(--headline-text);
    font-size: 112px;
    font-weight: 700;
    letter-spacing: 1px;
    line-height: 1;
  }
  .tagline__band--find { background: var(--band-black); }
  .tagline__band--your { background: var(--band-blue); }
  .tagline__band--game { background: var(--band-coral); }
  .locations-map {
    position: absolute;
    left: 100px;
    top: 590px;
    width: 560px;
    height: 260px;
    border-radius: 6px;
    background: linear-gradient(160deg, var(--map-light) 0%, var(--map-mid) 100%);
  }
  .brand {
    position: absolute;
    right: 70px;
    bottom: 90px;
    display: flex;
    align-items: center;
    gap: 14px;
  }
  .brand__mark {
    width: 62px;
    height: 62px;
    border-radius: 10px;
    background: var(--brand-orange);
  }
  .brand__name {
    font-size: 30px;
    font-weight: 700;
    color: var(--ink);
    line-height: 1.05;
    width: 170px;
  }
  .site-address {
    position: absolute;
    right: 70px;
    bottom: 56px;
    font-size: 17px;
    font-weight: 700;
    color: var(--ink);
  }
</style>
</head>
<body>
  <main class="poster">
    <h1 class="tagline">
      <span class="tagline__band tagline__band--find">FIND</span>
      <span class="tagline__band tagline__band--your">YOUR</span>
      <span class="tagline__band tagline__band--game">GAME</span>
    </h1>
    <div class="locations-map" role="img" aria-label="Folded city map with blue location pins and one highlighted red pin"></div>
    <div class="brand">
      <div class="brand__mark"></div>
      <div class="brand__name">Pixel Haven Spots</div>
    </div>
    <p class="site-address">www.pixelhavenspots.com</p>
  </main>
</body>
</html>
```